London Based Property Finding Company - have logo already

We find property for private purchasers and investors in London, UK.  We work for the BUYER, whereas estate agencies/real estate companies work for the seller. We offer a much more personalised service to UK and overseas purchasers.

We would like the following:

*A double sided business card

*A letterhead

We have attached two versions of the logo. Each logo style is set on two different coloured backgrounds. Please choose one of the two designs, whichever you prefer or feel more comfortable with, and produce one in black and one in white background.

This applies to both pieces of stationery.

THE BUSINESS CARD:

We would like the company name placed on its own on one side of the card and the contact details and what we do on the other.

e.g.

SIDE 1:

BRAMWELL PROPERTY FINDERS

SIDE 2:

Owen Bramwell

t: 0208 394 2860

m: +44(0)7932 418 507

e: info@bramwellpropertyfinders.co.uk

w: bramwellpropertyfinders.co.uk

London Property Finders and Search Agents

I will leave the layout up to you, but a minimalist layout is preferred. If you would like to put additional detial or design on the card then that is up to, but not specified.

It is optional to have the company name on side 2, but if you do use it, please make it smaller. than on the 1st side.

The design needs to be simple, professional and not too in your face.

If you are using the black background design on side 1 for the logo, then maybe a white backgounnd can be used on side 2 with a black typeface.

The type face for the contacts details should be sans serif standard typeface. Please experiment with the desciprtion.

-

THE LETTERHEAD;

You can experiment with the layout for the letterhead. e.g logo centre aligned on the top of the page with the contact details and address at the bottom of the page OR the logo, description running along a bar on the top of the page with the contact details and website address at the bottom. Please try and experiment with this, but the less 'busy', the better.

Here is info that needs to be on the letterhead.

Bramwell Property Finders

t: 0208 394 2860

m: +44(0)7932 418 507

(PLEASE NOTE; the below company info must be placed at the bottom of the page as a footer, in small text.)

Kestrand Holdings Ltd Trading as Bramwell Property Finders, a company registered in England & Wales, No.7351926 , Registered office is 41 Hollinmoor Court, Hollinmoor Road, London, SW9 3PL, t: 0208 394 2860, m: +44(0)7932 418 507, e: info@bramwellpropertyfinders.co.uk

Best of luck!

Thank you

Dear Designer,

I have now attached the supporting files to this brief.

Thanks,

Owen Bramwell
Bramwell Property Finders

```html
<!DOCTYPE html>
<html lang="en">
<head>
<meta charset="utf-8">
<title>Bramwell Property Finders – Stationery</title>
<link href="https://fonts.googleapis.com/css2?family=EB+Garamond:wght@400;500&family=Arimo:wght@400;700&display=swap" rel="stylesheet">
<style>
  :root {
    --navy: #1f2e5c;
    --ink: #1a1a1a;
    --grey: #6b6b6b;
    --skyline: #ececec;
    --paper: #ffffff;
    --card-light: #fdfdfb;
    --card-dark: #0a0a0a;
    --frame: #9a9a9a;
  }
  * { box-sizing: border-box; margin: 0; padding: 0; }
  html, body {
    width: 1200px; height: 1122px; overflow: hidden;
    background: var(--paper);
  }
  body { position: relative; font-family: "Arimo", Arial, sans-serif; }

  .letterhead {
    position: absolute; left: 33px; top: 54px; width: 711px; height: 1002px;
    border: 1px solid var(--frame); background: var(--paper);
  }
  .skyline {
    position: absolute;
    background: linear-gradient(to bottom, rgba(236,236,236,0.6), var(--skyline));
  }
  .letterhead .skyline { left: 12px; top: 12px; width: 690px; height: 42px; }

  .wordmark {
    position: absolute; font-family: "EB Garamond", Garamond, serif;
    font-weight: 500; color: var(--navy); letter-spacing: 0.04em;
    white-space: nowrap; transform: translateX(-50%);
  }
  .letterhead .wordmark { left: 50%; top: 76px; font-size: 25px; }

  .letter-contacts {
    position: absolute; left: 0; right: 0; top: 893px; text-align: center;
  }
  .letter-contacts .company { font-weight: 700; color: var(--navy); font-size: 13px; }
  .letter-contacts .lines { color: var(--ink); font-size: 12.5px; margin-top: 2px; }

  .legal {
    position: absolute; left: 52px; top: 941px;
    color: var(--grey); font-size: 10.5px; line-height: 15px;
  }

  .card {
    position: absolute; width: 402px; height: 253px; border-radius: 22px;
    overflow: hidden;
  }
  .card-front {
    left: 767px; top: 227px; background: var(--card-light);
    border: 1px solid var(--frame);
  }
  .card-front .wordmark { left: 50%; top: 112px; font-size: 22px; }
  .card-front .skyline { left: 14px; top: 207px; width: 372px; height: 24px; }

  .card-back {
    left: 771px; top: 522px; background: var(--card-dark); color: #fff;
  }
  .card-back .tagline {
    position: absolute; left: 0; right: 0; top: 23px; text-align: center;
    font-family: "EB Garamond", Garamond, serif; font-size: 12.5px;
  }
  .card-back .holder {
    position: absolute; left: 0; right: 0; top: 104px; text-align: center;
    font-family: "EB Garamond", Garamond, serif; font-size: 19px; letter-spacing: 0.04em;
  }
  .card-back .details {
    position: absolute; top: 196px; font-size: 9.5px; line-height: 13px;
  }
  .details.phones { left: 58px; }
  .details.online { left: 180px; }
</style>
</head>
<body>
  <section class="letterhead">
    <div class="skyline" role="img" aria-label="Faint London skyline silhouette"></div>
    <div class="wordmark">BRAMWELL PROPERTY FINDERS</div>
    <div class="letter-contacts">
      <p class="company">Bramwell Property Finders</p>
      <p class="lines">t: 0208 394 2860;&nbsp; m: +44(0) 7932 418 507&nbsp; e: info@bramwellpropertyfinders.co.uk&nbsp; w: bramwellpropertyfinders.co.uk</p>
    </div>
    <div class="legal">
      <p>Kestrand Holdings Ltd Trading as Bramwell Property Finders, a company registered in England &amp; Wales, No.7351926</p>
      <p>Registered office is 41 Hollinmoor Court, Hollinmoor Road, London SW9 3PL, t: 0208 394 2860, m: +44(0) 7932 418 507</p>
      <p>e: info@bramwellpropertyfinders.co.uk</p>
    </div>
  </section>

  <section class="card card-front">
    <div class="wordmark">BRAMWELL PROPERTY FINDERS</div>
    <div class="skyline" role="img" aria-label="Faint London skyline silhouette"></div>
  </section>

  <section class="card card-back">
    <p class="tagline">London Property Finders and Search Agents</p>
    <p class="holder">OWEN BRAMWELL</p>
    <div class="details phones">
      <p>t: 0208 394 2860</p>
      <p>m: +44(0)7932 418 507</p>
    </div>
    <div class="details online">
      <p>e: info@bramwellpropertyfinders.com</p>
      <p>w: bramwellpropertyfinders.co.uk</p>
    </div>
  </section>
</body>
</html>
```